Digital One Pager for Consulting Practice

I would like the essence of the content in my ppt consolidated into a one-pager. The one-pager will mainly be sent via email as a pdf and intended to excite and invite new clients and establish the credibility of my boutique high-end consulting firm. Infographics and symbols would be a plus. The target client should view the firm as providing premeir service. The client is getting a thought partner.

Target Market(s)

Large Medical Device Manufacturer Executives, Early-Stage Medical Device Manufacturer Executives, Partners at VC Firms

Industry/Entity Type

Medical Equipment

Colors
0355a3
f37122

Requirements
Must have
• Please match the color scheme in ppt. Please use the existing logo. I am very open to better graphics on the process. My photo does not need to be on the digital flyer. Hyper link to the website and email is needed.
Nice to have
• Infographics

```html
<!DOCTYPE html>
<html lang="en">
<head>
<meta charset="utf-8">
<title>Halden Ventures – One Pager</title>
<link rel="stylesheet" href="https://fonts.googleapis.com/css2?family=Bebas+Neue&family=Lato:ital,wght@0,400;0,700;0,900;1,400;1,700&family=Tinos:ital,wght@1,700&display=swap">
<style>
  :root {
    --red: #ee4136;
    --navy: #0f1a2e;
    --ink: #1d1f2a;
    --white: #ffffff;
    --mint: #7fe0c0;
    --leverage: #153a6a;
    --partner: #b9bec8;
  }
  * { box-sizing: border-box; margin: 0; padding: 0; }
  html, body { width: 902px; height: 1200px; overflow: hidden; background: var(--white); }
  body { font-family: "Lato", sans-serif; color: var(--ink); }

  .sheet { position: relative; width: 902px; height: 1200px; overflow: hidden; background: var(--white); }

  .hero-shapes, .hero-photo { position: absolute; left: 0; top: 0; }

  .brand {
    position: absolute; left: 0; top: 112px; width: 355px;
    display: flex; align-items: center; justify-content: center; gap: 12px;
  }
  .brand-square { width: 22px; height: 22px; background: var(--navy); }
  .brand-name {
    font-family: "Lato", sans-serif; font-weight: 900; color: var(--navy);
    font-size: 30px; letter-spacing: 3px; line-height: 1;
  }

  .headline {
    position: absolute; left: 28px; top: 262px; width: 310px;
    font-family: "Bebas Neue", sans-serif; font-weight: 400; text-transform: uppercase;
    line-height: 1.12; white-space: nowrap;
  }
  .headline span { display: block; }
  .headline .dark { color: var(--ink); }
  .headline .light { color: var(--white); }
  .headline .l1 { font-size: 40px; letter-spacing: 0.2px; }
  .headline .l2 { font-size: 48px; }
  .headline .l3 { font-size: 48px; letter-spacing: 0.5px; }

  .offer { position: absolute; left: 53px; top: 618px; width: 400px; }
  .offer h2 {
    color: var(--red); font-weight: 700; font-size: 21px; line-height: 1.25;
    text-transform: uppercase; margin-bottom: 10px;
  }
  .offer ul { list-style: none; margin-bottom: 16px; }
  .offer li {
    position: relative; padding-left: 18px; font-style: italic; font-size: 13.5px;
    line-height: 1.35; margin-bottom: 8px;
  }
  .offer li::before {
    content: ""; position: absolute; left: 0; top: 5px; width: 8px; height: 8px;
    border-radius: 50%; background: var(--red);
  }
  .offer .lead { color: var(--red); display: block; }
  .offer .detail { font-weight: 700; display: block; }

  .differentiators { position: absolute; left: 470px; top: 600px; width: 380px; height: 300px; }
  .differentiators h3 {
    text-align: center; font-weight: 400; font-size: 20px; letter-spacing: 0.5px; color: var(--ink);
  }
  .venn { display: block; margin-top: 4px; }
  .venn-label { font-family: "Tinos", serif; font-style: italic; font-weight: 700; font-size: 15px; fill: var(--white); text-decoration: underline; }
  .venn-center { text-decoration: none; }

  .process-title {
    position: absolute; left: 53px; top: 906px; font-weight: 900; font-size: 16px; text-transform: uppercase;
  }
  .process { position: absolute; left: 30px; top: 938px; width: 842px; display: flex; align-items: center; }
  .step {
    width: 194px; height: 94px; background: var(--red);
    display: flex; flex-direction: column; align-items: center; justify-content: center;
    text-transform: uppercase; text-align: center; line-height: 1.02;
    box-shadow: 0 7px 6px -4px rgba(0,0,0,0.35);
  }
  .step .top { color: var(--white); font-weight: 900; font-size: 25px; }
  .step .bottom { color: var(--ink); font-weight: 900; font-size: 25px; }
  .step .small { font-size: 17px; }
  .step .huge { font-size: 44px; }
  .step .big { font-size: 32px; }
  .arrow { width: 22px; display: flex; justify-content: center; }

  .footer {
    position: absolute; left: 0; top: 1062px; width: 902px; height: 138px;
    background: linear-gradient(180deg, #d6d6d6 0%, #f4f4f4 35%, #ffffff 100%);
  }
  .contact-bar {
    position: absolute; left: 53px; top: 1046px; width: 805px; height: 56px; background: #0b0b0b;
    display: flex; align-items: center; justify-content: space-around; padding: 0 20px;
    color: var(--white); font-weight: 700; font-size: 20px;
  }
  .contact-bar a { color: var(--white); text-decoration: none; display: flex; align-items: center; gap: 8px; }
  .partners { position: absolute; left: 34px; top: 1138px; width: 840px; display: flex; align-items: center; gap: 20px; }
  .partners-label { font-size: 13px; font-weight: 700; line-height: 1.2; width: 100px; color: var(--ink); }
  .partner { background: var(--partner); height: 34px; }
</style>
</head>
<body>
<main class="sheet">

  <svg class="hero-shapes" width="902" height="600" viewBox="0 0 902 600" aria-hidden="true">
    <rect width="902" height="596" fill="var(--navy)"/>
    <polygon points="0,492 902,570 902,574 0,502" fill="var(--white)"/>
    <polygon points="0,504 902,578 902,592 0,546" fill="var(--red)"/>
  </svg>

  <svg class="hero-photo" width="902" height="600" viewBox="0 0 902 600" role="img" aria-label="Photo of an open laptop, headphones, books and a coffee cup on a bright white desk">
    <defs>
      <linearGradient id="photoTone" x1="0" y1="0" x2="1" y2="1">
        <stop offset="0" stop-color="#f4f5f6"/>
        <stop offset="0.55" stop-color="#d9dbde"/>
        <stop offset="1" stop-color="#a9adb2"/>
      </linearGradient>
    </defs>
    <polygon points="335,0 902,0 902,582 410,536 395,445 335,445" fill="url(#photoTone)"/>
  </svg>

  <svg class="hero-shapes" width="902" height="600" viewBox="0 0 902 600" aria-hidden="true">
    <rect x="0" y="205" width="355" height="238" fill="var(--red)"/>
    <polygon points="0,66 355,66 355,205 178,247 0,205" fill="var(--white)"/>
  </svg>

  <div class="brand">
    <span class="brand-square"></span>
    <span class="brand-name">HALDEN<br>VENTURES</span>
  </div>

  <h1 class="headline">
    <span class="dark l1">Extensive Experience</span>
    <span class="light l2">Efficient Process</span>
    <span class="dark l3">Valued Network</span>
  </h1>

  <section class="offer">
    <h2>Experience to provide...</h2>
    <ul>
      <li><span class="lead">Examples include:</span><span class="detail">Presubmission, IDE, 510(k), 513(g), PMA,<br>Refuse to Accept, Hold letter</span></li>
      <li>Troubleshooting</li>
    </ul>
    <h2>Strategic advice &amp; diligence<br>to investors</h2>
    <ul>
      <li>Validate &amp; Verify Founder Milestones</li>
      <li>Diligence portfolio company<br>Regulatory and Quality systems</li>
    </ul>
  </section>

  <section class="differentiators">
    <h3>DIFFERENTIATORS</h3>
    <svg class="venn" width="380" height="280" viewBox="0 0 380 280" aria-label="Experience, network and process overlapping around leverage">
      <defs>
        <linearGradient id="ball" x1="0" y1="0" x2="0" y2="1">
          <stop offset="0" stop-color="#d8d8d8"/>
          <stop offset="1" stop-color="#6f6f6f"/>
        </linearGradient>
      </defs>
      <circle cx="98" cy="92" r="86" fill="url(#ball)" stroke="var(--mint)" stroke-width="2"/>
      <circle cx="278" cy="92" r="86" fill="url(#ball)" stroke="var(--mint)" stroke-width="2"/>
      <circle cx="188" cy="196" r="86" fill="url(#ball)" stroke="var(--mint)" stroke-width="2"/>
      <circle cx="180" cy="112" r="50" fill="var(--leverage)" stroke="var(--mint)" stroke-width="1.5"/>
      <text class="venn-label" x="64" y="96" text-anchor="middle">Experience</text>
      <text class="venn-label" x="305" y="96" text-anchor="middle">Network</text>
      <text class="venn-label" x="188" y="226" text-anchor="middle">Process</text>
      <text class="venn-label venn-center" x="180" y="117" text-anchor="middle">Leverage</text>
    </svg>
  </section>

  <h3 class="process-title">Efficient Process</h3>
  <div class="process">
    <div class="step"><span class="top small">Exploratory</span><span class="bottom huge">Call</span></div>
    <div class="arrow"><svg width="18" height="12" viewBox="0 0 18 12"><path d="M0 6h12M10 1l6 5-6 5z" stroke="#000" stroke-width="2.5" fill="#000"/></svg></div>
    <div class="step"><span class="top">Regulatory</span><span class="bottom">Landscape</span></div>
    <div class="arrow"><svg width="18" height="12" viewBox="0 0 18 12"><path d="M0 6h12M10 1l6 5-6 5z" stroke="#000" stroke-width="2.5" fill="#000"/></svg></div>
    <div class="step"><span class="top big">Problem</span><span class="bottom">Statement</span></div>
    <div class="arrow"><svg width="18" height="12" viewBox="0 0 18 12"><path d="M0 6h12M10 1l6 5-6 5z" stroke="#000" stroke-width="2.5" fill="#000"/></svg></div>
    <div class="step"><span class="top">Review &amp;</span><span class="top">Align on</span><span class="bottom small">Deliverables</span></div>
  </div>

  <footer class="footer"></footer>
  <div class="contact-bar">
    <a href="https://www.haldenventures.com">
      <svg width="18" height="18" viewBox="0 0 18 18"><circle cx="9" cy="9" r="7.5" fill="none" stroke="var(--red)" stroke-width="1.8"/><path d="M1.5 9h15M9 1.5c-4 4-4 11 0 15M9 1.5c4 4 4 11 0 15" fill="none" stroke="var(--red)" stroke-width="1.4"/></svg>
      www.haldenventures.com</a>
    <a href="tel:5550142290">
      <svg width="18" height="18" viewBox="0 0 18 18"><circle cx="9" cy="9" r="7.5" fill="none" stroke="var(--red)" stroke-width="1.8"/><path d="M6 5l2 2-1 1.2c.6 1.2 1.6 2.2 2.8 2.8L11 10l2 2-1.2 1.2C9 13 5 9 4.8 6.2z" fill="var(--red)"/></svg>
      555.014.2290</a>
    <a href="mailto:info@haldenventures.com">
      <svg width="20" height="14" viewBox="0 0 20 14"><rect width="20" height="14" fill="var(--red)"/><path d="M1 1l9 7 9-7" fill="none" stroke="#0b0b0b" stroke-width="1.6"/></svg>
      info@haldenventures.com</a>
  </div>

  <div class="partners">
    <span class="partners-label">Valued Partner<br>Network</span>
    <span class="partner" style="width:100px;height:14px"></span>
    <span class="partner" style="width:78px"></span>
    <span class="partner" style="width:82px"></span>
    <span class="partner" style="width:64px;height:28px"></span>
    <span class="partner" style="width:58px;height:28px"></span>
    <span class="partner" style="width:70px;height:30px"></span>
  </div>

</main>
</body>
</html>
```